K&T Holdings

Design a modern simple business card. I have attached a clean version of a card we like form Marrowfield Partners another company we own. I also attached the old K&T card design and logo and a couple of ideas we had but just can't finalize on whether we like them or not. We would like to include the 20 year logo somewhere on the card.

```html
<!DOCTYPE html>
<html lang="en">
<head>
<meta charset="utf-8">
<title>K&amp;T Holdings – Business Card</title>
<link href="https://fonts.googleapis.com/css2?family=Arimo:wght@400;700&family=Montserrat:wght@500&display=swap" rel="stylesheet">
<style>
  :root {
    --navy: #23205f;
    --white: #ffffff;
    --grey-text: #8a8a8a;
    --ink: #2b2b3a;
    --stage: #2e2e2e;
  }
  * { box-sizing: border-box; margin: 0; padding: 0; }
  html, body { width: 1200px; height: 875px; overflow: hidden; }
  body {
    background: var(--stage);
    font-family: "Arimo", Arial, sans-serif;
    position: relative;
  }
  .card {
    position: absolute;
    left: 290px;
    width: 620px;
    height: 354px;
    border-radius: 22px;
    overflow: hidden;
  }
  .card--front { top: 64px; background: var(--navy); color: var(--white); }
  .card--back { top: 458px; background: var(--white); }

  /* front */
  .front-brand {
    position: absolute; left: 70px; top: 138px;
    font-size: 78px; font-weight: 700; letter-spacing: -1px;
    display: flex; align-items: center; gap: 14px;
  }
  .front-brand .dot {
    width: 18px; height: 18px; border-radius: 50%; background: var(--white);
  }
  .front-divider {
    position: absolute; left: 318px; top: 82px; width: 1px; height: 190px;
    background: rgba(255,255,255,0.8);
  }
  .anniversary {
    position: absolute; left: 356px; top: 102px;
    font-family: "Montserrat", Arial, sans-serif; font-weight: 500;
    color: var(--white);
  }
  .anniversary .years-count { font-size: 92px; line-height: 1; }
  .anniversary .years-label { font-size: 22px; letter-spacing: 4px; margin-top: 4px; }
  .anniversary .years-range { font-size: 26px; letter-spacing: 2px; margin-top: 4px; }

  /* back */
  .back-brand {
    position: absolute; right: 40px; top: 30px;
    color: var(--navy); font-size: 34px; font-weight: 700;
    display: flex; align-items: center; gap: 8px;
  }
  .back-brand .dot { width: 10px; height: 10px; border-radius: 50%; background: var(--navy); }
  .person { position: absolute; left: 46px; top: 196px; }
  .person-name { color: var(--navy); font-size: 31px; font-weight: 700; }
  .person-title { color: var(--grey-text); font-size: 19px; text-align: right; margin-top: 2px; }
  .back-divider {
    position: absolute; left: 322px; top: 120px; width: 2px; height: 142px;
    background: var(--navy);
  }
  .contact { position: absolute; left: 344px; top: 120px; color: var(--ink); font-size: 14px; line-height: 1.4; }
  .contact-company { color: var(--navy); font-weight: 700; font-size: 16px; letter-spacing: 0.3px; }
  .contact-address { margin-bottom: 6px; }
  .contact-list { list-style: none; }
  .contact-list li { display: flex; align-items: center; gap: 8px; }
  .contact-list svg { width: 12px; height: 12px; flex: none; }
</style>
</head>
<body>

<section class="card card--front" aria-label="Card front">
  <div class="front-brand"><span class="dot"></span>K&amp;T</div>
  <div class="front-divider"></div>
  <div class="anniversary">
    <div class="years-count">20</div>
    <div class="years-label">YEARS</div>
    <div class="years-range">2004-2024</div>
  </div>
</section>

<section class="card card--back" aria-label="Card back">
  <div class="back-brand"><span class="dot"></span>K&amp;T</div>

  <div class="person">
    <div class="person-name">Daniel Harlow</div>
    <div class="person-title">IT Director</div>
  </div>

  <div class="back-divider"></div>

  <div class="contact">
    <div class="contact-company">K&amp;T HOLDINGS</div>
    <div class="contact-address">412 Cedar Avenue, Suite 208<br>Lakemont, TX 77540</div>
    <ul class="contact-list">
      <li>
        <svg viewBox="0 0 24 24" aria-hidden="true"><path fill="var(--navy)" d="M6.6 10.8a15 15 0 0 0 6.6 6.6l2.2-2.2a1 1 0 0 1 1-.25 11.4 11.4 0 0 0 3.6.57 1 1 0 0 1 1 1V20a1 1 0 0 1-1 1A17 17 0 0 1 3 4a1 1 0 0 1 1-1h3.5a1 1 0 0 1 1 1c0 1.25.2 2.45.57 3.6a1 1 0 0 1-.25 1z"/></svg>
        555-210-4837
      </li>
      <li>
        <svg viewBox="0 0 24 24" aria-hidden="true"><rect x="6" y="2" width="12" height="20" rx="2" fill="none" stroke="var(--navy)" stroke-width="2.4"/><circle cx="12" cy="18" r="1.3" fill="var(--navy)"/></svg>
        555-318-2764
      </li>
      <li>
        <svg viewBox="0 0 24 24" aria-hidden="true"><rect x="2" y="5" width="20" height="14" rx="1.5" fill="var(--navy)"/><path d="M3 6l9 7 9-7" fill="none" stroke="var(--white)" stroke-width="1.8"/></svg>
        dharlow@kthltd.com
      </li>
      <li>
        <svg viewBox="0 0 24 24" aria-hidden="true"><circle cx="12" cy="12" r="9" fill="none" stroke="var(--navy)" stroke-width="2.4"/><path d="M3 12h18M12 3c3 3.5 3 14.5 0 18M12 3c-3 3.5-3 14.5 0 18" fill="none" stroke="var(--navy)" stroke-width="1.6"/></svg>
        www.kthltd.com
      </li>
    </ul>
  </div>
</section>

</body>
</html>
```